The Brightwater Compass Business Card

We need an attractive business card with the logo that we bought from ArtVantly last year.
Our mission is to contribute to change the way today's leaders manage business companies bringing value to the workplace and helping them to build a new model of creating wealth.
Our logo is clear about our values : we seek Positive Change through People and are convinced that the pursuit of individual well-being and the chase of economic results can converge with the right management.
Management Consulting
Corinne Fabrelle
+34 612 98 70 31
corinne.fabrelle@thebrightwatercompass-mail.net
www.thebrightwatercompass-mail.net

```html
<!DOCTYPE html>
<html lang="en">
<head>
<meta charset="utf-8">
<title>The Brightwater Compass – Business Card</title>
<link rel="stylesheet" href="https://fonts.googleapis.com/css2?family=Poppins:wght@400;600&display=swap">
<style>
  :root {
    --backdrop: #e7e7e7;
    --teal: #08898a;
    --teal-soft: #5ea9a8;
    --teal-ink: #2b8585;
    --paper: #ffffff;
    --shadow: rgba(0, 0, 0, 0.18);
  }
  * { box-sizing: border-box; margin: 0; padding: 0; }
  html, body {
    width: 1200px;
    height: 900px;
    overflow: hidden;
    background: var(--backdrop);
    font-family: "Poppins", sans-serif;
  }
  .stage {
    position: relative;
    width: 1200px;
    height: 900px;
  }
  .card {
    position: absolute;
    width: 560px;
    height: 320px;
    box-shadow: 0 6px 18px var(--shadow);
  }
  .card--front {
    left: 110px;
    top: 110px;
    background: var(--teal);
    display: flex;
    align-items: center;
    justify-content: center;
  }
  .brand {
    display: flex;
    align-items: center;
    gap: 14px;
    color: var(--teal-soft);
    font-weight: 600;
    font-size: 28px;
    letter-spacing: 0.06em;
    text-transform: uppercase;
  }
  .brand__dot {
    width: 22px;
    height: 22px;
    border-radius: 50%;
    background: var(--teal-soft);
  }
  .card--back {
    left: 530px;
    top: 470px;
    background: var(--paper);
    overflow: hidden;
  }
  .symbol-area {
    position: absolute;
    left: 0;
    top: 0;
    width: 200px;
    height: 190px;
    background: radial-gradient(circle at 40% 45%, #7ab8b7 0%, #cfe6e5 70%, rgba(255,255,255,0) 100%);
  }
  .contact {
    position: absolute;
    left: 150px;
    bottom: 34px;
    color: var(--teal-ink);
    font-size: 12.5px;
    font-weight: 400;
    letter-spacing: 0.16em;
    line-height: 1.55;
  }
  .contact__name {
    font-weight: 600;
    font-size: 13.5px;
  }
</style>
</head>
<body>
  <main class="stage">
    <section class="card card--front">
      <div class="brand">
        <span class="brand__dot"></span>
        <span class="brand__name">The Brightwater Compass</span>
      </div>
    </section>

    <section class="card card--back">
      <div class="symbol-area" role="img" aria-label="Brand symbol area in teal tones"></div>
      <div class="contact">
        <p class="contact__name">Corinne Fabrelle</p>
        <p class="contact__phone">+34 612 98 70 31</p>
        <p class="contact__email">corinne.fabrelle@thebrightwatercompass-mail.net</p>
        <p class="contact__web">www.thebrightwatercompass-mail.net</p>
      </div>
    </section>
  </main>
</body>
</html>
```